Ledge Crafts one page flyer

We need a standard A4 size flyer for a new company called Ledge Crafts. We are a construction material company and sell trims, crown mouldings, baseboards and panelings.
We would like to see the design with the following information:
1. Size: A4
2. Only one front page, no design need to display on back
3. Logo (Ledge Crafts, see the attached EPS file)
4. Slogan: We offer high quality products for competitive prices.
5. Content please see the PDF file
6. The production has 2 category, one called "Crown Moulding", the other is "Wainscoting", Crown Moulding has 5 productions, wainscoting has 2 production(Details see PDF file)
6. We temporary only can provide low resolution images for 7 productions, only the winner will be provided with High Resolution images.
Look and feel
Each slider illustrates characteristics of the customer's brand and the style your logo design should communicate.

```html
<!DOCTYPE html>
<html lang="en">
<head>
<meta charset="utf-8">
<title>Ledge Crafts Flyer</title>
<link href="https://fonts.googleapis.com/css2?family=Raleway:wght@500;600;700&family=Montserrat:wght@500;700&family=Playball&display=swap" rel="stylesheet">
<style>
:root{
  --bg-light:#efe6d8;
  --bg-mid:#e2d5c2;
  --bg-deep:#cfbfa8;
  --ink:#4f4238;
  --accent:#d84a2b;
  --size-blue:#2f52a3;
  --footer-ink:#4a4039;
  --profile:#f6f2ec;
  --profile-shade:#d9d2c8;
}
*{margin:0;padding:0;box-sizing:border-box}
html,body{width:927px;height:1200px;overflow:hidden;background:var(--bg-light)}
.flyer{position:relative;width:927px;height:1200px;overflow:hidden;font-family:"Montserrat",sans-serif;color:var(--ink)}
.room-backdrop{position:absolute;inset:0;background:
  radial-gradient(ellipse at 50% 40%,rgba(255,250,240,.75),rgba(255,250,240,0) 60%),
  linear-gradient(180deg,var(--bg-light) 0%,var(--bg-mid) 55%,var(--bg-deep) 80%,var(--bg-light) 100%)}
.brand{position:absolute;top:46px;left:0;width:927px;text-align:center;font-family:"Raleway",sans-serif;font-weight:600;font-size:30px;line-height:1;color:var(--ink)}
.headline{position:absolute;top:148px;left:0;width:927px;text-align:center;font-family:"Raleway",sans-serif;font-weight:600;font-size:36px;line-height:48px;color:var(--ink);text-transform:uppercase}
.category-title{position:absolute;top:312px;font-family:"Playball",cursive;font-size:46px;font-weight:400;color:var(--accent);line-height:1}
.cat-crown{left:121px}
.cat-wains{left:617px}
.product{position:absolute;width:400px;height:74px}
.profile{position:absolute;left:0;top:0;width:72px;height:72px;background:linear-gradient(135deg,var(--profile),var(--profile-shade))}
.product-name{position:absolute;top:10px;left:104px;font-family:"Playball",cursive;font-size:24px;color:var(--ink);white-space:nowrap;line-height:1.1}
.product-size{position:absolute;top:48px;left:104px;font-weight:700;font-size:16px;color:var(--size-blue);white-space:nowrap}
.footer{position:absolute;top:1052px;left:0;width:927px;height:148px;font-size:14px;color:var(--footer-ink);line-height:24px}
.footer-block{position:absolute;top:0;display:flex;gap:14px}
.footer-icon{width:46px;height:46px;flex:none;margin-top:4px}
.hours{left:30px}
.hours p{line-height:31px}
.office{left:336px}
.warehouse{left:656px}
</style>
</head>
<body>
<div class="flyer">
  <div class="room-backdrop" role="img" aria-label="Softly lit interior room with crown moulding, wainscoting panels, a chandelier and wood floor"></div>

  <header class="brand">Ledge Crafts</header>

  <h1 class="headline">We offer high quality products<br>for competitive prices</h1>

  <h2 class="category-title cat-crown">Crown Moulding</h2>
  <h2 class="category-title cat-wains">Wainscoting</h2>

  <section class="col-left">
    <div class="product" style="left:48px;top:406px">
      <div class="profile" role="img" aria-label="Siena 9 crown moulding profile sample"></div>
      <div class="product-name">Siena 9 Crown Moulding</div>
      <div class="product-size">8 7/16"x 3/4"</div>
    </div>
    <div class="product" style="left:48px;top:513px">
      <div class="profile" role="img" aria-label="Siena 8 crown moulding profile sample"></div>
      <div class="product-name">Siena 8 Crown Moulding</div>
      <div class="product-size">7 3/4"x 3/4"</div>
    </div>
    <div class="product" style="left:48px;top:620px">
      <div class="profile" role="img" aria-label="Siena 7 crown moulding profile sample"></div>
      <div class="product-name">Siena 7 Crown Moulding</div>
      <div class="product-size">6 1/2"x 3/4"</div>
    </div>
    <div class="product" style="left:48px;top:727px">
      <div class="profile" role="img" aria-label="Verona 8 crown moulding profile sample"></div>
      <div class="product-name">Verona 8 Crown Moulding</div>
      <div class="product-size">7 3/4"x 3/4"</div>
    </div>
    <div class="product" style="left:48px;top:834px">
      <div class="profile" role="img" aria-label="Verona 6 crown moulding profile sample"></div>
      <div class="product-name">Verona 6 Crown Moulding</div>
      <div class="product-size">6 1/4"x 3/4"</div>
    </div>
  </section>

  <section class="col-right">
    <div class="product" style="left:533px;top:406px">
      <div class="profile" role="img" aria-label="Heritage chair rail profile sample"></div>
      <div class="product-name">Heritage Chair Rail</div>
      <div class="product-size">3 1/4"x 1"</div>
    </div>
    <div class="product" style="left:533px;top:513px">
      <div class="profile" role="img" aria-label="Heritage panel mould profile sample"></div>
      <div class="product-name">Heritage Panel Mould</div>
      <div class="product-size">1 3/4"x 5/8"</div>
    </div>
  </section>

  <footer class="footer">
    <div class="footer-block hours">
      <svg class="footer-icon" viewBox="0 0 46 46" aria-hidden="true">
        <circle cx="23" cy="23" r="21" fill="var(--accent)"/>
        <circle cx="23" cy="23" r="14" fill="none" stroke="var(--bg-light)" stroke-width="3"/>
        <path d="M23 14v10h7" fill="none" stroke="var(--bg-light)" stroke-width="3" stroke-linecap="round"/>
      </svg>
      <div>
        <p>Mon – Fri: 7:00am – 6.00pm</p>
        <p>Saturdays: 8:00am – 4.00pm</p>
        <p>Sundays: Closed</p>
      </div>
    </div>
    <div class="footer-block office">
      <svg class="footer-icon" viewBox="0 0 46 46" aria-hidden="true">
        <path d="M23 3c-8.3 0-15 6.5-15 14.6C8 28.5 23 43 23 43s15-14.5 15-25.4C38 9.5 31.3 3 23 3z" fill="none" stroke="var(--accent)" stroke-width="3"/>
        <circle cx="23" cy="17.5" r="5.5" fill="none" stroke="var(--accent)" stroke-width="3"/>
      </svg>
      <div>
        <p>Office:</p>
        <p>417 Maple Grove Ave, unit 2</p>
        <p>Lakeview Hill, Ontario L5C 2K8</p>
        <p>Phone: 905-555-0142</p>
        <p>info@ledgecrafts.ca</p>
      </div>
    </div>
    <div class="footer-block warehouse">
      <svg class="footer-icon" viewBox="0 0 46 46" aria-hidden="true">
        <path d="M23 5L3 22h6v18h10V29h8v11h10V22h6z" fill="var(--accent)"/>
      </svg>
      <div>
        <p>Warehouse:</p>
        <p>228 Birchfield Dr</p>
        <p>Eastmoor, ON M4K 1R6</p>
        <p>By Appointment Only</p>
      </div>
    </div>
  </footer>
</div>
</body>
</html>
```